Outdoor Real Estate Sales Banner

It should say

418 Calloway Street, East Boston
Coming Spring 2026
3 Luxury Condos
Experience refined living with elegant design and high-end finishes. Thoughtfully crafted for both comfort and sophistication.
Construction by V Construction
Now Accepting Reservations

Schedule Your Private Tour Today
Marisol Fenwick, Lanternwick Realty | 555-014-2273 | Marisol@lanternwickhomes.com
Tobias Grant, Lanternwick Realty | 555-019-8831 | Tobias@lanternwickhomes.com

Target Market(s)

30-45

Industry/Entity Type

real estate

Font styles to use
Serif

Requirements
Must have
• Colors of logo and preppy rich look
Nice to have
• herringbone incorporated the pattern
Should not have
• any loud colors

```html
<!DOCTYPE html>
<html lang="en">
<head>
<meta charset="utf-8">
<title>418 Calloway Street – Coming Spring 2026</title>
<link href="https://fonts.googleapis.com/css2?family=Cinzel:wght@400;500;600;700&display=swap" rel="stylesheet">
<style>
  :root {
    --navy: #1f2d4f;
    --navy-deep: #1a2644;
    --gold: #e2bc6a;
    --gold-light: #f3d794;
    --gold-dark: #b98f3c;
    --white: #ffffff;
  }
  html, body {
    margin: 0;
    padding: 0;
    width: 1200px;
    height: 720px;
    overflow: hidden;
    background: var(--navy);
  }
  .banner {
    position: relative;
    width: 1200px;
    height: 720px;
    overflow: hidden;
    background: radial-gradient(ellipse at 50% 40%, var(--navy) 0%, var(--navy-deep) 100%);
    font-family: "Cinzel", serif;
  }
  .top-band {
    position: absolute;
    left: 0; top: 0;
    width: 1200px; height: 16px;
    background: linear-gradient(90deg, var(--gold-dark), var(--gold-light) 45%, var(--gold) 70%, var(--gold-dark));
  }
  .headlines {
    position: absolute;
    left: 0; top: 0;
  }
  .agent-photo {
    position: absolute;
    z-index: 2;
  }
  .agent-photo--left {
    left: 60px; top: 440px; width: 203px; height: 206px;
    background: linear-gradient(160deg, #d9d4c8 0%, #a9a293 45%, #3d3a36 100%);
  }
  .agent-photo--right {
    left: 954px; top: 441px; width: 204px; height: 198px;
    background: linear-gradient(180deg, #8fa27a 0%, #c9b8a2 50%, #2f3a4f 100%);
  }
  .intro {
    position: absolute;
    left: 262px; top: 440px; width: 680px;
    margin: 0;
    text-align: center;
    color: var(--white);
    font-size: 16.2px;
    line-height: 21px;
    text-transform: uppercase;
    letter-spacing: 0.1px;
  }
  .feature {
    position: absolute;
    margin: 0;
    color: var(--gold);
    font-size: 22px;
    font-weight: 600;
    line-height: 29px;
    letter-spacing: 3px;
    text-align: center;
    font-variant: small-caps;
  }
  .feature--builder { left: 270px; top: 494px; width: 290px; }
  .feature--reserve { left: 640px; top: 494px; width: 290px; }
  .tour-call {
    position: absolute;
    left: 260px; top: 576px; width: 680px;
    margin: 0;
    text-align: center;
    color: var(--white);
    font-size: 23px;
    text-transform: uppercase;
    letter-spacing: 0.3px;
  }
  .footer-band {
    position: absolute;
    left: 0; top: 609px;
    width: 1200px; height: 111px;
    background: linear-gradient(90deg, #c89d4a 0%, #e4bb68 30%, #ebc575 50%, #d9ad58 75%, #c39646 100%);
    border-top: 2px solid var(--gold-light);
  }
  .agent-contact {
    position: absolute;
    top: 645px;
    margin: 0;
    color: var(--white);
    font-size: 16px;
    line-height: 22px;
    text-transform: uppercase;
    z-index: 3;
  }
  .agent-contact--left { left: 23px; text-align: left; }
  .agent-contact--right { right: 22px; text-align: right; }
  .brand-name {
    position: absolute;
    left: 470px; top: 664px; width: 260px;
    margin: 0;
    text-align: center;
    color: var(--white);
    font-size: 18px;
    font-weight: 400;
    line-height: 22px;
    text-transform: uppercase;
    z-index: 3;
  }
</style>
</head>
<body>
<main class="banner">
  <div class="top-band"></div>

  <svg class="headlines" width="1200" height="420" viewBox="0 0 1200 420" aria-label="418 Calloway Street, East Boston. Coming Spring 2026. 3 Luxury Condos">
    <defs>
      <linearGradient id="goldFill" x1="0" y1="0" x2="0" y2="1">
        <stop offset="0" stop-color="#f6dc9a"/>
        <stop offset="0.5" stop-color="#e6c173"/>
        <stop offset="1" stop-color="#c99a45"/>
      </linearGradient>
      <linearGradient id="ruleFill" x1="0" y1="0" x2="1" y2="0">
        <stop offset="0" stop-color="#c99a45"/>
        <stop offset="0.5" stop-color="#f3d794"/>
        <stop offset="1" stop-color="#c99a45"/>
      </linearGradient>
    </defs>
    <g fill="url(#goldFill)" font-family="Cinzel, serif" font-weight="600">
      <text class="street-number" x="166" y="199" font-size="190" textLength="306" lengthAdjust="spacingAndGlyphs">418</text>
      <text class="street-name" x="491" y="131" font-size="104" textLength="550" lengthAdjust="spacingAndGlyphs">CALLOWAY</text>
      <text class="street-city" x="489" y="197" font-size="55" textLength="545" lengthAdjust="spacingAndGlyphs">STREET, EAST BOSTON</text>
      <text class="headline" x="54" y="398" font-size="118" textLength="1072" lengthAdjust="spacingAndGlyphs">3 LUXURY CONDOS</text>
    </g>
    <rect x="73" y="259" width="294" height="7" rx="3" fill="url(#ruleFill)"/>
    <rect x="835" y="259" width="295" height="7" rx="3" fill="url(#ruleFill)"/>
    <text class="launch-date" x="600" y="280" text-anchor="middle" fill="#ffffff" font-family="Cinzel, serif" font-weight="500" font-size="44" textLength="450" lengthAdjust="spacingAndGlyphs">COMING SPRING 2026</text>
  </svg>

  <div class="agent-photo agent-photo--left" role="img" aria-label="Portrait photo of agent Marisol Fenwick in a bright interior"></div>
  <div class="agent-photo agent-photo--right" role="img" aria-label="Portrait photo of agent Tobias Grant outdoors"></div>

  <p class="intro">Experience refined living with elegant design &amp; high-end finishes.<br>Thoughtfully crafted for both comfort and sophistication.</p>
  <p class="feature feature--builder">Construction by<br>V Construction</p>
  <p class="feature feature--reserve">Now Accepting<br>Reservations</p>
  <p class="tour-call">Schedule Your Private Tour Today</p>

  <div class="footer-band"></div>

  <p class="agent-contact agent-contact--left">Marisol Fenwick, Lanternwick Realty<br>| 555-014-2273 | Marisol@lanternwickhomes.com</p>
  <p class="brand-name">Lanternwick Realty</p>
  <p class="agent-contact agent-contact--right">Tobias Grant, Lanternwick Realty<br>| 555-019-8831 | Tobias@lanternwickhomes.com</p>
</main>
</body>
</html>
```